Dorrish Electric Ltd

Looking for a single page website and Pagebook page design. I am an electrical contractor based on Vancouver Island. I do service, custom homes, residential and commercial installations. My company just started out, so I don't have any pictures of installs yet. I have 25 years experience. I would like the colors to be my logo colors black and I have a black Corvan Ridgeback that will be my vehicle which I will have a wrap for.
Updates

I just posted the contest today, not sure why the deadline is the same day.

Went on vacation/holiday

Industry/Entity Type

Electrician

Requirements
Must have
• Services provided, About me section, quote section,
Nice to have
• I am not quite sure yet, I need to see some designs first .

```html
<!DOCTYPE html>
<html lang="en">
<head>
<meta charset="utf-8">
<title>Dorrish Electric Ltd – Page Design</title>
<link rel="stylesheet" href="https://fonts.googleapis.com/css2?family=Roboto:wght@400;500;700&display=swap">
<style>
:root{
  --stage:#e4e5e9;
  --page:#e9ebee;
  --bar:#4267b2;
  --bar-dark:#1e3d7a;
  --panel:#ffffff;
  --line:#dddfe2;
  --text:#1d2129;
  --muted:#90949c;
  --icon:#606770;
  --link:#365899;
  --gold:#f5b80c;
  --ink:#0b0b0b;
  --green:#42b72a;
}
*{box-sizing:border-box;margin:0;padding:0}
html,body{width:1200px;height:1024px;overflow:hidden}
body{background:var(--stage);font-family:"Roboto",Arial,sans-serif;color:var(--text);position:relative}
.abs{position:absolute}
.sheet{left:67px;top:68px;width:1065px;height:888px;background:var(--page);box-shadow:0 4px 14px rgba(0,0,0,.18)}
.topbar{left:67px;top:68px;width:1065px;height:30px;background:var(--bar)}
.brand-square{left:219px;top:73px;width:18px;height:18px;background:#fff;border-radius:2px}
.search{left:243px;top:73px;width:337px;height:18px;background:#fff;border-radius:2px;font-size:11px;line-height:18px;padding-left:5px}
.search svg{position:absolute;right:8px;top:3px}
.bar-user{left:736px;top:73px;width:18px;height:18px;border-radius:50%;background:#f1c3b5}
.bar-text{top:76px;color:#fff;font-size:10px;font-weight:700}
.bar-sep{top:76px;width:1px;height:13px;background:#2f4f92}
.badge{left:918px;top:72px;width:14px;height:10px;background:#fa3e3e;color:#fff;font-size:7px;text-align:center;line-height:10px;border-radius:2px}
.avatar{left:218px;top:110px;width:134px;height:134px;border-radius:50%;background:var(--ink);border:4px solid #fff;box-shadow:0 0 0 1px var(--line);display:flex;align-items:center;justify-content:center}
.avatar span{color:#fff;font-size:8.5px;font-weight:500;margin-top:52px}
.page-name{left:219px;top:258px;font-size:15px}
.page-handle{left:219px;top:280px;font-size:11px;color:var(--muted);font-weight:500}
.nav-home{left:216px;top:303px;width:140px;height:22px;background:#fff;border:1px solid var(--line);font-weight:700;font-size:10.5px;padding:5px 6px}
.nav-item{left:222px;font-size:10.5px;color:#4b4f56}
.create{left:219px;top:482px;width:73px;height:18px;background:var(--green);color:#fff;font-size:9px;font-weight:700;text-align:center;line-height:18px;border-radius:2px}
.cover{left:365px;top:98px;width:620px;height:237px;background:
 radial-gradient(ellipse 170px 120px at 190px 95px,#d9621a 0%,#6a2a0c 45%,transparent 75%),
 linear-gradient(90deg,#2a2a2a,#151515 60%,#0e0e0e)}
.cover-name{left:668px;top:218px;width:294px;text-align:center;color:#fff;font-size:26px;font-weight:500;white-space:nowrap}
.cover-web{left:705px;top:251px;width:224px;height:17px;background:var(--gold);border-radius:4px;font-size:11px;letter-spacing:3.2px;text-align:center;line-height:17px;color:var(--ink);font-weight:500}
.actionbar{left:365px;top:335px;width:620px;height:40px;background:#fff;border:1px solid var(--line);border-top:none}
.btn-group{left:374px;top:344px;height:21px;display:flex;border:1px solid #ccd0d5;background:#f5f6f7;border-radius:2px}
.btn-group div{padding:0 8px;font-size:9.5px;font-weight:700;color:#4b4f56;line-height:19px;border-right:1px solid #ccd0d5;display:flex;align-items:center;gap:4px}
.btn-group div:last-child{border-right:none}
.learn{left:758px;top:344px;width:106px;height:21px;background:var(--bar);color:#fff;font-size:11px;text-align:center;line-height:21px;border-radius:2px}
.send{left:873px;top:344px;width:104px;height:21px;border:1px solid #ccd0d5;background:#f5f6f7;color:#4b4f56;font-size:11px;line-height:19px;text-align:center;border-radius:2px}
.box{background:#fff;border:1px solid var(--line);border-radius:3px}
.status{left:365px;top:385px;width:378px;height:82px}
.status-head{height:26px;background:#f6f7f9;border-bottom:1px solid var(--line);font-size:9.5px;font-weight:500;padding:7px 0 0 28px;color:#4b4f56}
.mini{border-radius:50%;background:var(--ink);border:1px solid #444}
.posts{left:365px;top:476px;width:378px;height:454px}
.posts-title{left:374px;top:485px;font-size:11px;font-weight:700}
.post{left:374px;top:505px;width:361px;height:416px;background:#fff;border:1px solid var(--line)}
.post-author{left:420px;top:517px;font-size:11px;color:var(--link);font-weight:500}
.post-time{left:420px;top:533px;font-size:9px;color:var(--muted)}
.post-text{left:383px;top:552px;width:340px;font-size:10.3px;line-height:14px}
.post-img{left:374px;top:591px;width:361px;height:230px;background:radial-gradient(circle 90px at 185px 100px,#f4a52a 0%,#a3520e 40%,#2b1406 75%,#120904 100%)}
.post-imgname{left:384px;top:650px;color:#fff;font-size:8px;font-weight:500}
.post-web{left:384px;top:797px;color:#fff;font-size:7px;letter-spacing:2.4px}
.post-action{top:832px;font-size:10.5px;font-weight:500;color:var(--icon);display:flex;align-items:center;gap:5px}
.post-rule{left:374px;top:853px;width:361px;height:1px;background:var(--line)}
.likes{left:383px;top:860px;font-size:9px;color:var(--link);display:flex;align-items:center;gap:3px}
.comment{left:413px;top:889px;width:311px;height:25px;border:1px solid #ccd0d5;border-radius:13px;font-size:10px;color:var(--muted);padding:6px 8px}
.rpanel{left:752px;width:233px}
.rtitle{font-size:10.5px;font-weight:700}
.row{left:763px;font-size:9px;display:flex;align-items:center;gap:8px}
.row svg{flex:none}
.lnk{color:var(--link);font-weight:500}
.seeall{font-size:9px;color:var(--link)}
.liked{width:66px;height:18px;border:1px solid #ccd0d5;background:#f5f6f7;font-size:9px;font-weight:700;color:#4b4f56;display:flex;align-items:center;justify-content:center;gap:3px}
.pname{font-size:10.5px;font-weight:700}
.divider{height:1px;background:var(--line)}
</style>
</head>
<body>
<div class="abs sheet"></div>
<div class="abs topbar"></div>
<div class="abs brand-square"></div>
<div class="abs search">Pagebook Page Template
  <svg width="11" height="11" viewBox="0 0 12 12"><circle cx="5" cy="5" r="3.8" fill="none" stroke="#4b4f56" stroke-width="1.4"/><line x1="8" y1="8" x2="11" y2="11" stroke="#4b4f56" stroke-width="1.4"/></svg>
</div>
<div class="abs bar-user"></div>
<div class="abs bar-text" style="left:759px">Brightmark</div>
<div class="abs bar-sep" style="left:819px"></div>
<div class="abs bar-text" style="left:827px">Home</div>
<div class="abs bar-sep" style="left:859px"></div>
<svg class="abs" style="left:863px;top:75px" width="17" height="14" viewBox="0 0 17 14"><circle cx="5.5" cy="4" r="3" fill="var(--bar-dark)"/><path d="M0 13c0-3.5 2.5-5 5.5-5s5.5 1.5 5.5 5z" fill="var(--bar-dark)"/><circle cx="12" cy="4" r="2.6" fill="var(--bar-dark)"/><path d="M11.5 8c3 0 5.5 1.3 5.5 5h-5z" fill="var(--bar-dark)"/></svg>
<svg class="abs" style="left:889px;top:75px" width="15" height="14" viewBox="0 0 15 14"><path d="M7.5 0C3.4 0 0 2.9 0 6.5c0 2 1 3.7 2.6 4.9V14l2.6-1.4c.7.2 1.5.3 2.3.3 4.1 0 7.5-2.9 7.5-6.4S11.6 0 7.5 0z" fill="var(--bar-dark)"/></svg>
<svg class="abs" style="left:914px;top:75px" width="14" height="14" viewBox="0 0 14 14"><circle cx="7" cy="7" r="7" fill="var(--bar-dark)"/><path d="M1.5 7h11M7 1v12" stroke="#4267b2" stroke-width="1"/></svg>
<div class="abs badge">7</div>
<svg class="abs" style="left:951px;top:75px" width="14" height="14" viewBox="0 0 14 14"><circle cx="7" cy="7" r="7" fill="var(--bar-dark)"/><text x="7" y="10.5" font-size="10" font-weight="700" text-anchor="middle" fill="#fff" font-family="Roboto,Arial,sans-serif">?</text></svg>
<svg class="abs" style="left:977px;top:79px" width="8" height="5"><path d="M0 0h8L4 5z" fill="var(--bar-dark)"/></svg>

<!-- left column -->
<div class="abs avatar"><span>DORRISH ELECTRIC Ltd</span></div>
<div class="abs page-name">Pagebook</div>
<div class="abs page-handle">@pagebook</div>
<div class="abs nav-home">Home</div>
<div class="abs nav-item" style="top:332px">About</div>
<div class="abs nav-item" style="top:356px">Photos</div>
<div class="abs nav-item" style="top:381px">Reviews</div>
<div class="abs nav-item" style="top:405px">Events</div>
<div class="abs nav-item" style="top:429px">Posts</div>
<div class="abs nav-item" style="top:454px">Community</div>
<div class="abs create">Create a Page</div>

<!-- cover -->
<div class="abs cover" role="img" aria-label="Cover photo: a hand reaching toward a light bulb bursting with fiery sparks on a dark background"></div>
<div class="abs cover-name">DORRISH ELECTRIC Ltd</div>
<div class="abs cover-web">www.dorrishelectric.ca</div>

<div class="abs actionbar"></div>
<div class="abs btn-group">
  <div><svg width="9" height="9" viewBox="0 0 10 10"><path d="M0 4h2v6H0zM3 4l3-4c1 0 1.5.6 1.3 1.5L7 3.5h2.5c.5 0 .8.5.7 1L9 9.5c-.1.3-.4.5-.7.5H3z" fill="#606770"/></svg>Like</div>
  <div><svg width="9" height="9" viewBox="0 0 10 10"><circle cx="1.5" cy="8.5" r="1.3" fill="#606770"/><path d="M0 4.5a5.5 5.5 0 0 1 5.5 5.5M0 1a9 9 0 0 1 9 9" fill="none" stroke="#606770" stroke-width="1.3"/></svg>Follow</div>
  <div><svg width="10" height="9" viewBox="0 0 10 9"><path d="M6 0l4 4-4 4V5.5C3 5.5 1.2 6.5 0 9c.3-3.5 2.5-5.5 6-6z" fill="#606770"/></svg>Share</div>
  <div>···</div>
</div>
<div class="abs learn">Learn More</div>
<div class="abs send">Send Message</div>

<!-- status -->
<div class="abs box status"><div class="status-head">Status</div></div>
<svg class="abs" style="left:377px;top:392px" width="11" height="11" viewBox="0 0 10 10"><path d="M7 0l3 3-6 6H1V6z" fill="#4267b2"/></svg>
<div class="abs mini" style="left:705px;top:390px;width:13px;height:13px"></div>
<svg class="abs" style="left:721px;top:395px" width="6" height="4"><path d="M0 0h6L3 4z" fill="#606770"/></svg>
<div class="abs mini" style="left:374px;top:420px;width:31px;height:31px"></div>
<div class="abs" style="left:413px;top:429px;font-size:10.5px;color:var(--muted)">Write something on this Page...</div>

<!-- posts -->
<div class="abs box posts"></div>
<div class="abs posts-title">Posts</div>
<div class="abs post"></div>
<div class="abs mini" style="left:383px;top:515px;width:32px;height:32px"></div>
<div class="abs post-author">Voltspire</div>
<div class="abs post-time">18 hrs</div>
<svg class="abs" style="left:453px;top:533px" width="10" height="10" viewBox="0 0 10 10"><circle cx="5" cy="5" r="4.2" fill="none" stroke="#90949c" stroke-width="1.2"/><path d="M1 5h8M5 1v8" stroke="#90949c" stroke-width=".8"/></svg>
<div class="abs" style="left:714px;top:513px;font-size:12px;font-weight:700;color:#606770">···</div>
<div class="abs post-text">Your post message text goes in this area, you can edit it easily according to your needs, enjoy.</div>
<div class="abs post-img" role="img" aria-label="Glowing light bulb filament throwing orange sparks against a dark background"></div>
<div class="abs post-imgname">DORRISH ELECTRIC Ltd</div>
<div class="abs post-web">www.dorrishelectric.ca</div>

<div class="abs post-action" style="left:415px"><svg width="14" height="13" viewBox="0 0 14 13"><path d="M1 6h2.5v6H1zM4.5 6l3.2-5c1 0 1.6.8 1.3 1.8L8.5 4.5h3.6c.7 0 1.1.6 1 1.2l-1 5.6c-.1.4-.5.7-.9.7H4.5z" fill="none" stroke="#606770" stroke-width="1.1"/></svg>Like</div>
<div class="abs post-action" style="left:504px"><svg width="13" height="12" viewBox="0 0 13 12"><path d="M1.5 1h10a1 1 0 0 1 1 1v6a1 1 0 0 1-1 1H6l-3 2.5V9H1.5a1 1 0 0 1-1-1V2a1 1 0 0 1 1-1z" fill="none" stroke="#606770" stroke-width="1.1"/></svg>Comment</div>
<div class="abs post-action" style="left:615px"><svg width="14" height="12" viewBox="0 0 14 12"><path d="M8.5 1l4.8 4.5-4.8 4.5V7.4C5 7.4 2.6 8.5 1 11c.5-4.3 3.2-6.6 7.5-7z" fill="none" stroke="#606770" stroke-width="1.1" stroke-linejoin="round"/></svg>Share</div>
<svg class="abs" style="left:712px;top:836px" width="7" height="4"><path d="M0 0h7L3.5 4z" fill="#606770"/></svg>
<div class="abs post-rule"></div>
<div class="abs likes"><svg width="12" height="12"><circle cx="6" cy="6" r="6" fill="#4267b2"/><path d="M3 5h1.5v4H3zM5 5l2-2.5c.6 0 .8.4.7 1L7.5 4.5h1.3c.3 0 .5.3.4.6L8.6 8.6c0 .2-.2.4-.4.4H5z" fill="#fff"/></svg>82</div>
<div class="abs mini" style="left:381px;top:887px;width:30px;height:30px"></div>
<div class="abs comment">Write a comment..</div>

<!-- right column -->
<div class="abs box rpanel" style="top:385px;height:30px"></div>
<svg class="abs" style="left:763px;top:395px" width="11" height="11" viewBox="0 0 12 12"><circle cx="5" cy="5" r="3.8" fill="none" stroke="#90949c" stroke-width="1.4"/><line x1="8" y1="8" x2="11" y2="11" stroke="#90949c" stroke-width="1.4"/></svg>
<div class="abs" style="left:783px;top:394px;font-size:9.5px;color:var(--muted)">Search for posts on this Page</div>

<div class="abs box rpanel" style="top:424px;height:125px"></div>
<div class="abs rtitle" style="left:761px;top:433px">Community</div>
<div class="abs seeall" style="left:948px;top:435px">See All</div>
<div class="abs row" style="top:458px"><svg width="12" height="10" viewBox="0 0 17 14"><circle cx="5.5" cy="4" r="3" fill="#90949c"/><path d="M0 13c0-3.5 2.5-5 5.5-5s5.5 1.5 5.5 5z" fill="#90949c"/><circle cx="12" cy="4" r="2.6" fill="#90949c"/><path d="M11.5 8c3 0 5.5 1.3 5.5 5h-5z" fill="#90949c"/></svg><span><span class="lnk">Invite your friends</span> to like this Page</span></div>
<div class="abs row" style="top:479px"><svg width="12" height="11" viewBox="0 0 10 10"><path d="M0 4h2v6H0zM3 4l3-4c1 0 1.5.6 1.3 1.5L7 3.5h2.5c.5 0 .8.5.7 1L9 9.5c-.1.3-.4.5-.7.5H3z" fill="#90949c"/></svg>107,476 people like this</div>
<div class="abs row" style="top:500px"><svg width="12" height="11" viewBox="0 0 10 10"><circle cx="1.5" cy="8.5" r="1.3" fill="#90949c"/><path d="M0 4.5a5.5 5.5 0 0 1 5.5 5.5M0 1a9 9 0 0 1 9 9" fill="none" stroke="#90949c" stroke-width="1.3"/></svg>99,000 people follow this</div>
<div class="abs row" style="top:522px"><svg width="12" height="10" viewBox="0 0 17 14"><circle cx="5.5" cy="4" r="3" fill="#90949c"/><path d="M0 13c0-3.5 2.5-5 5.5-5s5.5 1.5 5.5 5z" fill="#90949c"/><circle cx="12" cy="4" r="2.6" fill="#90949c"/><path d="M11.5 8c3 0 5.5 1.3 5.5 5h-5z" fill="#90949c"/></svg><span><span class="lnk">Mira Tallen</span> likes This</span></div>

<div class="abs box rpanel" style="top:558px;height:74px"></div>
<div class="abs rtitle" style="left:761px;top:566px">About</div>
<div class="abs seeall" style="left:948px;top:568px">See All</div>
<div class="abs row lnk" style="top:589px"><svg width="12" height="12" viewBox="0 0 12 12"><path d="M6 1C3 1 .8 3.1.8 5.7c0 1.4.6 2.6 1.7 3.5V11l1.8-1c.5.2 1.1.3 1.7.3 3 0 5.2-2.1 5.2-4.6S9 1 6 1z" fill="none" stroke="#606770" stroke-width="1"/></svg>Contact Brightmark on Chat</div>
<div class="abs row" style="top:611px;color:var(--link)"><svg width="12" height="11" viewBox="0 0 12 11"><rect x=".5" y="1.5" width="11" height="9" fill="none" stroke="#606770" stroke-width="1"/><path d="M.5 4h11" stroke="#606770" stroke-width="1"/></svg>Education</div>

<div class="abs box rpanel" style="top:642px;height:74px"></div>
<div class="abs rtitle" style="left:761px;top:650px">People</div>
<svg class="abs" style="left:972px;top:653px" width="6" height="10"><path d="M1 1l4 4-4 4" fill="none" stroke="#606770" stroke-width="1.4"/></svg>
<div class="abs divider" style="left:752px;top:671px;width:233px"></div>
<div class="abs" style="left:836px;top:685px;font-size:13px;font-weight:700">107k <span style="font-size:9.5px;font-weight:400;color:var(--muted)">likes</span></div>

<div class="abs box rpanel" style="top:726px;height:203px"></div>
<div class="abs rtitle" style="left:761px;top:734px">Pages liked by this page</div>
<svg class="abs" style="left:972px;top:737px" width="6" height="10"><path d="M1 1l4 4-4 4" fill="none" stroke="#606770" stroke-width="1.4"/></svg>
<div class="abs divider" style="left:752px;top:754px;width:233px"></div>
<div class="abs mini" style="left:760px;top:763px;width:42px;height:42px"></div>
<div class="abs pname" style="left:809px;top:776px">Artists</div>
<div class="abs liked" style="left:908px;top:775px">✓ Liked ▾</div>
<div class="abs divider" style="left:752px;top:813px;width:233px"></div>
<div class="abs mini" style="left:760px;top:820px;width:42px;height:42px"></div>
<div class="abs pname" style="left:809px;top:834px">Developers</div>
<div class="abs liked" style="left:908px;top:834px">✓ Liked ▾</div>
<div class="abs divider" style="left:752px;top:871px;width:233px"></div>
<div class="abs mini" style="left:760px;top:880px;width:42px;height:42px"></div>
<div class="abs pname" style="left:809px;top:892px">Designers</div>
<div class="abs liked" style="left:908px;top:893px">✓ Liked ▾</div>
</body>
</html>
```